Vantrel Ashcombe LLC

we need a business card design

Industry/Entity Type

hvac

Contact Information for Business Card

my logo

Requirements
Must have
• my logo and same colors

```html
<!DOCTYPE html>
<html lang="en">
<head>
<meta charset="utf-8">
<title>Vantrel Ashcombe LLC — Business Card</title>
<link href="https://fonts.googleapis.com/css2?family=Poppins:wght@400;500;600;700&display=swap" rel="stylesheet">
<style>
  :root {
    --bg: #2b2b2b;
    --brand-blue: #1467b3;
    --brand-blue-light: #2a7cc6;
    --card-yellow: #fcbd5d;
    --ink: #1b1b1b;
    --rule: #c9953f;
    --white: #ffffff;
  }
  * { box-sizing: border-box; margin: 0; padding: 0; }
  html, body { width: 1200px; height: 800px; overflow: hidden; }
  body {
    background: var(--bg);
    font-family: "Poppins", sans-serif;
    display: flex;
    align-items: center;
    justify-content: center;
    gap: 60px;
  }
  .card {
    width: 520px;
    height: 300px;
    border-radius: 16px;
    position: relative;
    overflow: hidden;
  }
  /* Front */
  .card--front {
    background: radial-gradient(circle at 55% 35%, var(--brand-blue-light), var(--brand-blue) 75%);
    display: flex;
    align-items: center;
    justify-content: center;
  }
  .brand-name {
    font-weight: 700;
    color: var(--white);
    font-size: 34px;
    line-height: 1.15;
    text-align: center;
    display: flex;
    align-items: center;
    gap: 14px;
  }
  .brand-mark {
    width: 22px; height: 22px;
    background: var(--card-yellow);
    border-radius: 50%;
    flex: none;
  }
  /* Back */
  .card--back { background: var(--card-yellow); }
  .person {
    position: absolute;
    right: 40px;
    top: 34px;
    text-align: right;
  }
  .person__name {
    color: var(--brand-blue);
    font-weight: 700;
    font-size: 26px;
    line-height: 1.1;
  }
  .person__title {
    color: var(--ink);
    font-weight: 600;
    font-size: 12px;
    letter-spacing: 0.3px;
    margin-top: 2px;
  }
  .title-tab {
    position: absolute;
    right: 0; top: 30px;
    width: 10px; height: 44px;
    background: var(--brand-blue);
  }
  .divider {
    position: absolute;
    left: 30px; right: 30px;
    height: 1px;
    background: var(--rule);
  }
  .divider--top { top: 112px; left: 200px; }
  .divider--bottom { top: 200px; right: 200px; }
  .card--back .brand-name {
    position: absolute;
    left: 30px; top: 122px;
    color: var(--brand-blue);
    font-size: 22px;
    gap: 10px;
  }
  .card--back .brand-mark { width: 16px; height: 16px; background: var(--brand-blue); }
  .contacts {
    position: absolute;
    left: 30px; top: 212px;
    list-style: none;
    font-size: 13px;
    color: var(--ink);
    line-height: 1.35;
  }
  .contacts li { display: flex; align-items: flex-start; gap: 10px; margin-bottom: 4px; }
  .contact-icon {
    width: 16px; height: 16px; flex: none;
    background: var(--brand-blue);
    border-radius: 2px;
    display: flex; align-items: center; justify-content: center;
    margin-top: 1px;
  }
  .footer-band { position: absolute; left: 0; bottom: 0; width: 520px; height: 110px; }
  .website {
    position: absolute;
    right: 24px; bottom: 56px;
    color: var(--white);
    font-size: 13px;
    font-weight: 500;
    display: flex; align-items: center; gap: 6px;
  }
</style>
</head>
<body>
  <section class="card card--front" aria-label="Card front">
    <div class="brand-name"><span class="brand-mark"></span>Vantrel Ashcombe LLC</div>
  </section>

  <section class="card card--back" aria-label="Card back">
    <span class="title-tab"></span>
    <div class="person">
      <div class="person__name">Marcus Ellery</div>
      <div class="person__title">MANAGING DIRECTOR</div>
    </div>
    <span class="divider divider--top"></span>

    <div class="brand-name"><span class="brand-mark"></span>Vantrel Ashcombe LLC</div>

    <span class="divider divider--bottom"></span>

    <ul class="contacts">
      <li><span class="contact-icon"><svg width="10" height="10" viewBox="0 0 10 10"><path d="M2 1h2l1 2-1.2.8a5 5 0 0 0 2.4 2.4L7 5l2 1v2a1 1 0 0 1-1 1A7 7 0 0 1 1 2a1 1 0 0 1 1-1z" fill="#fff"/></svg></span>044-987 654 321</li>
      <li><span class="contact-icon"><svg width="10" height="10" viewBox="0 0 10 10"><path d="M1 5 9 1 6 9 5 6z" fill="#fff"/></svg></span>info@vantrelmail.com</li>
      <li><span class="contact-icon"><svg width="10" height="10" viewBox="0 0 10 10"><path d="M5 1a3 3 0 0 1 3 3c0 2-3 5-3 5S2 6 2 4a3 3 0 0 1 3-3z" fill="#fff"/><circle cx="5" cy="4" r="1" fill="#1467b3"/></svg></span>4471 Harbor Reach Blvd,<br>212-C, FL 33602</li>
    </ul>

    <svg class="footer-band" viewBox="0 0 520 110" aria-hidden="true">
      <path d="M300 110 L350 80 C365 70 360 40 400 40 L520 40 L520 110 Z" fill="var(--brand-blue)"/>
      <path d="M0 110 L0 104 L340 96 L300 110 Z" fill="var(--brand-blue)"/>
    </svg>
    <div class="website">
      <svg width="12" height="12" viewBox="0 0 12 12"><circle cx="6" cy="6" r="5" fill="none" stroke="#fff" stroke-width="1.4"/><path d="M1 6h10M6 1c2 2 2 8 0 10M6 1c-2 2-2 8 0 10" fill="none" stroke="#fff" stroke-width="1"/></svg>
      www.vantrelashcombe.com
    </div>
  </section>
</body>
</html>
```